Bluegate Physiotherapy
Business Cards, Stationary, Letterhead, Magnet, Presentation Folder, A5 Referral Pad, Email Signatur
Bluegate Physiotherapy -
Creative Brief
Professional
Tom Ellingsworth
BSc Physiotherapy / Acupuncturist / Cert IV Occupational Health & Safety
Unit 3, 48 Kestrel Lane, Mandurah WA 6210
tom.ellingsworth@bluegatephysio-example.com.au
www.bluegatephysio-example.com.au
Magnet to be standard business card size (portrait OR landscape) and include only phone, address and website (in addition to graphic component). Referral pad to be A5 size. At the TOP: "Patient Name", "Date" as well as 4 tick boxes "W.C.", "Vet. Affairs", "Private" "EPC". At the BOTTOM: "Referring Doctor" "Sign" "Doctors Name" and "Address" as well as "Preferred Contact" with 4 tick boxes "E-mail", "Phone", "Fax", "Snail Mail". Down one SIDE to have a list: "Manual Therapy", "Massage", "Exercise Prescription", "Gym Based Rehab", "Workplace Assessment", "Ergonomics", "Acupuncture", "Sports Physiotherapy", "Womens Health".

```html
<!DOCTYPE html>
<html lang="en">
<head>
<meta charset="utf-8">
<title>Bluegate Physiotherapy – Stationery Set</title>
<link href="https://fonts.googleapis.com/css2?family=Open+Sans:wght@400;700&display=swap" rel="stylesheet">
<style>
:root{
  --bg:#e9e7e3;
  --paper:#ffffff;
  --ink:#2b2b2b;
  --muted:#7a7a7a;
  --blue:#1c8bc9;
  --green:#7ab83c;
  --orange:#f29122;
  --red:#d9312b;
  --black:#1d1c1c;
  --brown-1:#4a2c1c;
  --brown-2:#20140e;
  --shadow:0 2px 6px rgba(0,0,0,.18);
}
*{box-sizing:border-box;margin:0;padding:0}
html,body{width:1200px;height:734px;overflow:hidden}
body{background:var(--bg);font-family:"Open Sans",Arial,sans-serif;color:var(--ink);position:relative}
.piece{position:absolute;background:var(--paper);box-shadow:var(--shadow);overflow:hidden}
.piece--dark{background:var(--black);color:#ddd}

.brand{display:flex;align-items:center;gap:4px;font-weight:700;color:var(--blue);line-height:1.05}
.brand__dot{width:7px;height:7px;border-radius:50%;background:var(--orange);flex:none}
.brand__name{font-size:8px}
.piece--dark .brand{color:var(--paper)}

.swatches{position:absolute;display:flex;gap:2px}
.swatches i{display:block;width:5px;height:5px}
.swatches i:nth-child(1){background:var(--blue)}
.swatches i:nth-child(2){background:var(--green)}
.swatches i:nth-child(3){background:var(--orange)}
.swatches i:nth-child(4){background:var(--red)}

.tiny{font-size:5px;line-height:1.45;color:var(--muted)}
.tiny b{color:var(--ink)}
.piece--dark .tiny{color:#aaa}
.piece--dark .tiny b{color:#fff}

.card{width:154px;height:89px;padding:10px}
.card .brand{margin-bottom:10px}
.card .swatches{right:8px;bottom:8px}
.card--logo-only{display:flex;align-items:center;justify-content:center}
.card--logo-only .brand{margin:0}
.card--logo-only .brand__name{font-size:10px}

.letterhead{width:228px;height:322px;padding:16px}
.letterhead .head{display:flex;justify-content:space-between;align-items:flex-start}
.letterhead .brand__name{font-size:9px}
.letterhead .contact{text-align:left;width:86px}
.letterhead .footer{position:absolute;left:16px;right:16px;bottom:14px;border-top:1px solid #ccc;padding-top:4px}
.letterhead .swatches{right:16px;bottom:6px}

.referral{width:204px;height:281px;padding:12px;font-size:5px}
.referral .row{display:flex;gap:6px;margin-top:8px;align-items:flex-end}
.referral .field{flex:1;border-bottom:1px solid #bbb;padding-bottom:1px;color:var(--ink)}
.referral .ticks{display:flex;gap:8px;margin-top:8px}
.referral .ticks span{display:flex;align-items:center;gap:2px}
.referral .box{width:5px;height:5px;border:1px solid #888;display:inline-block}
.referral .body{display:flex;gap:8px;margin-top:10px}
.referral .services{width:64px;list-style:none;line-height:2}
.referral .services li{display:flex;align-items:center;gap:3px}
.referral .notes{flex:1;border-left:1px solid #ddd}
.referral .notes div{border-bottom:1px solid #e3e3e3;height:11px}
.referral .bottom{position:absolute;left:12px;right:12px;bottom:12px}

.envelope{width:300px;height:132px}
.envelope svg.flap{position:absolute;left:0;top:0}
.envelope .center-mark{position:absolute;left:50%;top:14px;transform:translateX(-50%)}
.envelope .sender{position:absolute;left:14px;bottom:12px}
.envelope .swatches{right:12px;bottom:12px}
.envelope--closed{width:264px}

.slip{width:312px;height:96px;padding:12px}
.slip .cols{display:flex;gap:18px;margin-top:8px}
.slip .swatches{right:12px;bottom:10px}

.folder{width:504px;height:336px;display:flex}
.folder__back{width:252px;height:100%;position:relative;
  background:linear-gradient(135deg,var(--brown-1),var(--brown-2))}
.folder__art{position:absolute;left:0;top:0;width:100%;height:75%;
  background:linear-gradient(160deg,#5a3622,var(--brown-1) 60%,transparent)}
.folder__back .back-info{position:absolute;left:14px;bottom:16px}
.folder__back .brand{position:absolute;right:14px;bottom:18px}
.folder__front{width:252px;height:100%;position:relative;background:var(--paper);border-left:1px solid #ddd;
  display:flex;justify-content:center;align-items:flex-start;padding-top:26px}
.folder__front .brand__name{font-size:11px}
.folder__front .swatches{right:14px;bottom:14px}
</style>
</head>
<body>

<div class="piece card" style="left:43px;top:43px">
  <div class="brand"><span class="brand__dot"></span><span class="brand__name">Bluegate<br>Physiotherapy</span></div>
  <p class="tiny"><b>Tom Ellingsworth</b><br>BSc Physiotherapy / Acupuncturist<br>Ph (08) 9555 0142 · M 0400 555 218</p>
  <div class="swatches"><i></i><i></i><i></i><i></i></div>
</div>
<div class="piece card" style="left:228px;top:43px">
  <p class="tiny"><b>(08) 9555 0142</b><br>Unit 3, 48 Kestrel Lane, Mandurah WA 6210<br>www.bluegatephysio-example.com.au</p>
  <div class="brand" style="margin-top:10px"><span class="brand__dot"></span><span class="brand__name">Bluegate<br>Physiotherapy</span></div>
  <div class="swatches"><i></i><i></i><i></i><i></i></div>
</div>
<div class="piece card" style="left:43px;top:151px">
  <p class="tiny"><b>(08) 9555 0142</b><br>Unit 3, 48 Kestrel Lane, Mandurah WA 6210</p>
  <div class="brand" style="margin-top:8px"><span class="brand__dot"></span><span class="brand__name">Bluegate<br>Physiotherapy</span></div>
  <p class="tiny">tom.ellingsworth@bluegatephysio-example.com.au</p>
  <div class="swatches"><i></i><i></i><i></i><i></i></div>
</div>
<div class="piece piece--dark card card--logo-only" style="left:228px;top:151px">
  <div class="brand"><span class="brand__dot"></span><span class="brand__name">Bluegate<br>Physiotherapy</span></div>
  <div class="swatches"><i></i><i></i><i></i><i></i></div>
</div>
<div class="piece card card--logo-only" style="left:43px;top:259px">
  <div class="brand"><span class="brand__dot"></span><span class="brand__name">Bluegate<br>Physiotherapy</span></div>
  <div class="swatches"><i></i><i></i><i></i><i></i></div>
</div>
<div class="piece piece--dark card card--logo-only" style="left:228px;top:259px">
  <div class="brand"><span class="brand__dot"></span><span class="brand__name">Bluegate<br>Physiotherapy</span></div>
  <div class="swatches"><i></i><i></i><i></i><i></i></div>
</div>

<div class="piece letterhead" style="left:408px;top:38px">
  <div class="head">
    <div class="brand"><span class="brand__dot"></span><span class="brand__name">Bluegate<br>Physiotherapy</span></div>
  </div>
  <p class="tiny footer">Unit 3, 48 Kestrel Lane, Mandurah WA 6210 · Ph (08) 9555 0142 · www.bluegatephysio-example.com.au</p>
  <div class="swatches"><i></i><i></i><i></i><i></i></div>
</div>
<div class="piece letterhead" style="left:672px;top:38px">
  <div class="head">
    <div class="brand"><span class="brand__dot"></span><span class="brand__name">Bluegate<br>Physiotherapy</span></div>
    <p class="tiny contact">Unit 3, 48 Kestrel Lane<br>Mandurah WA 6210<br>Ph (08) 9555 0142<br>Fax (08) 9555 0143<br>www.bluegatephysio-example.com.au</p>
  </div>
  <div class="swatches"><i></i><i></i><i></i><i></i></div>
</div>

<div class="piece referral" style="left:960px;top:43px">
  <div class="brand"><span class="brand__dot"></span><span class="brand__name">Bluegate Physiotherapy</span></div>
  <div class="row"><span class="field">Patient Name</span><span class="field" style="flex:.5">Date</span></div>
  <div class="ticks">
    <span><i class="box"></i>W.C.</span><span><i class="box"></i>Vet. Affairs</span><span><i class="box"></i>Private</span><span><i class="box"></i>EPC</span>
  </div>
  <div class="body">
    <ul class="services">
      <li><i class="box"></i>Manual Therapy</li><li><i class="box"></i>Massage</li><li><i class="box"></i>Exercise Prescription</li>
      <li><i class="box"></i>Gym Based Rehab</li><li><i class="box"></i>Workplace Assessment</li><li><i class="box"></i>Ergonomics</li>
      <li><i class="box"></i>Acupuncture</li><li><i class="box"></i>Sports Physiotherapy</li><li><i class="box"></i>Womens Health</li>
    </ul>
    <div class="notes"><div></div><div></div><div></div><div></div><div></div><div></div><div></div><div></div></div>
  </div>
  <div class="bottom">
    <div class="row"><span class="field">Referring Doctor</span><span class="field" style="flex:.6">Sign</span></div>
    <div class="row"><span class="field">Doctors Name</span></div>
    <div class="row"><span class="field">Address</span></div>
    <div class="ticks"><span>Preferred Contact</span><span><i class="box"></i>E-mail</span><span><i class="box"></i>Phone</span><span><i class="box"></i>Fax</span><span><i class="box"></i>Snail Mail</span></div>
  </div>
</div>

<div class="piece envelope" style="left:72px;top:372px">
  <svg class="flap" width="300" height="70" viewBox="0 0 300 70" aria-hidden="true">
    <path d="M0 0 L150 62 L300 0" fill="none" stroke="#d8d8d8" stroke-width="1"/>
  </svg>
  <div class="brand center-mark"><span class="brand__dot"></span><span class="brand__name">Bluegate Physiotherapy</span></div>
  <p class="tiny sender">Unit 3, 48 Kestrel Lane, Mandurah WA 6210 · www.bluegatephysio-example.com.au</p>
  <div class="swatches"><i></i><i></i><i></i><i></i></div>
</div>
<div class="piece envelope envelope--closed" style="left:396px;top:384px">
  <svg class="flap" width="264" height="60" viewBox="0 0 264 60" aria-hidden="true">
    <path d="M0 0 L132 52 L264 0" fill="none" stroke="#d8d8d8" stroke-width="1"/>
  </svg>
  <div class="brand center-mark"><span class="brand__dot"></span><span class="brand__name">Bluegate Physiotherapy</span></div>
  <div class="swatches"><i></i><i></i><i></i><i></i></div>
</div>

<div class="piece slip" style="left:72px;top:564px">
  <p class="tiny"><b style="font-size:7px">(08) 9555 0142</b><br>Unit 3, 48 Kestrel Lane, Mandurah WA 6210</p>
  <div class="cols">
    <div class="brand"><span class="brand__dot"></span><span class="brand__name">Bluegate<br>Physiotherapy</span></div>
    <p class="tiny">Ph (08) 9555 0142<br>Fax (08) 9555 0143</p>
    <p class="tiny">tom.ellingsworth@bluegatephysio-example.com.au<br>www.bluegatephysio-example.com.au</p>
  </div>
  <div class="swatches"><i></i><i></i><i></i><i></i></div>
</div>

<div class="piece folder" style="left:672px;top:384px">
  <div class="folder__back">
    <div class="folder__art" role="img" aria-label="Cover illustration area on a dark brown background"></div>
    <p class="tiny back-info">Unit 3, 48 Kestrel Lane<br>Mandurah WA 6210<br>(08) 9555 0142</p>
    <div class="brand"><span class="brand__dot"></span><span class="brand__name">Bluegate<br>Physiotherapy</span></div>
  </div>
  <div class="folder__front">
    <div class="brand"><span class="brand__dot"></span><span class="brand__name">Bluegate<br>Physiotherapy</span></div>
    <div class="swatches"><i></i><i></i><i></i><i></i></div>
  </div>
</div>

</body>
</html>
```